k eLiquid Label

We are an electronic cigarette eLiquid manufacturer with an outdated label design which needs to be updated and become more modern. All information listed on the label cannot be changed or removed.

There are 4 colour coding on the labels that cannot change.
0mg is white
12mg is yellow
18mg is blue
24mg is red

We prefer a blue type background however are not committed to it with the proper design however if a new colour is chosen it must compliment the colour band for each colour coding

The "dots" on the front of the bottle need to be larger.

The "V" on the front needs to be in this font however we can accept slight changes to it for effect.

Issues we are facing:
The 0mg and the 18mg look too close in colour and need to be completely different in colouring.

The background colouring is too dark and you cannot see the 50/50 in the watermark.

Reason: We have not received a design which is suitable to our needs. We have see a few close ones however not exact. Thanks

Reason: I was forced to go out of country for a family emergency and to be fair I am extending the deadline

```html
<!DOCTYPE html>
<html lang="en">
<head>
<meta charset="utf-8">
<title>k eLiquid Label – Sweet Tobacco</title>
<link href="https://fonts.googleapis.com/css2?family=Arimo:wght@400;700&family=Roboto:wght@300;400&display=swap" rel="stylesheet">
<style>
:root{
  --ink:#111;
  --paper:#fff;
  --zero:#ffffff;
  --yellow:#f5d21a;
  --blue:#1f5ea8;
  --red:#c8102e;
  --mist-light:#fafafa;
  --mist-dark:#b9b9b9;
  --watermark:rgba(255,255,255,.35);
}
*{margin:0;padding:0;box-sizing:border-box}
html,body{width:733px;height:1200px;overflow:hidden;background:var(--paper)}
body{position:relative;font-family:"Arimo",Arial,sans-serif;color:var(--ink)}

.label{position:absolute;left:0;width:733px;height:286px;--band:var(--zero);--band-ink:var(--ink);--mark:var(--zero)}
.label--zero{top:0}
.label--12{top:304px;--band:var(--yellow);--mark:var(--yellow)}
.label--18{top:610px;--band:var(--blue);--band-ink:#fff;--mark:var(--blue)}
.label--24{top:914px;--band:var(--red);--band-ink:#fff;--mark:var(--red)}

.band{position:absolute;left:0;width:100%;height:28px;background:var(--band);color:var(--band-ink);
  display:flex;justify-content:space-between;align-items:center;padding:0 16px;font-weight:700;font-size:15px;letter-spacing:.2px}
.band--top{top:0}
.band--bottom{bottom:0}

.hero{position:absolute;left:252px;top:28px;width:248px;height:230px;
  background:radial-gradient(ellipse at 55% 45%,var(--mist-light) 0%,#e2e2e2 45%,var(--mist-dark) 100%);overflow:hidden}
.hero__watermark{position:absolute;left:56px;top:-6px;font-family:"Roboto",sans-serif;font-weight:300;font-size:46px;line-height:40px;color:var(--watermark)}
.hero__strength{position:absolute;left:22px;top:108px;width:40px;height:40px;border-radius:50%;background:var(--mark)}
.label--zero .hero__strength{display:none}
.hero__name{position:absolute;left:66px;top:96px;font-family:"Arimo",sans-serif;font-weight:700;font-size:34px;color:var(--mark);white-space:nowrap}
.hero__volume{position:absolute;right:14px;top:152px;font-family:"Roboto",sans-serif;font-size:14px;color:#333}
.product{position:absolute;left:262px;top:224px;font-family:"Roboto",sans-serif;font-size:27px;line-height:1;letter-spacing:-.5px;white-space:nowrap}
.product__light{font-weight:300}
.product__bold{font-weight:400;font-family:"Arimo",sans-serif}

.warning{position:absolute;top:37px;font-size:13px;line-height:16.4px}
.warning--fr{right:483px;text-align:right;width:240px}
.warning--en{left:506px;width:225px}
.warning b{font-weight:700}
.producer{position:absolute;top:234px;font-size:9px;line-height:10.5px}
.producer--left{left:73px}
.producer--right{left:506px}

.hazard{position:absolute;left:10px;top:42px;width:28px;height:28px}
</style>
</head>
<body>

<!-- reusable panel structure, repeated four times -->
<section class="label label--zero">
  <div class="band band--top"><span>NICOTINE</span><span>FREE</span><span>NICOTINE</span><span>FREE</span><span>NICOTINE</span><span>FREE</span><span>NICOTINE</span><span>FREE</span><span>NICOTINE</span><span>FREE</span></div>
  <svg class="hazard" viewBox="0 0 28 28" aria-hidden="true"><polygon points="8,1 20,1 27,8 27,20 20,27 8,27 1,20 1,8" fill="none" stroke="#111" stroke-width="2"/><path d="M8 10 L20 20 M20 10 L8 20" stroke="#111" stroke-width="3" stroke-linecap="round"/></svg>
  <div class="warning warning--fr"><b>CONTENIR NOCIF</b><br>Do not swallow.<br>Do not get in eyes or skin or clothing.<br>Keep out of reach of children and pets.<br><b>INGREDIENTS:</b> Propylene Glucol,<br>Vegetable Glycerin, Nicotine (%),<br>Food Grade Alcohol, Natural and<br>Artificial flavours.<br><b>If swallowed consult poison control<br>centre or a doctor immediately.<br>May contain nuts.</b></div>
  <div class="hero"><div class="hero__watermark">50/50<br>50/50<br>50/50<br>50/50<br>50/50<br>50/50</div><div class="hero__strength"></div><div class="hero__name">k eLiquid</div><div class="hero__volume">zero · 30 ml</div></div>
  <div class="product"><span class="product__light">SWEET</span> <span class="product__bold">TOBACCO</span></div>
  <div class="warning warning--en"><b>WARNING CONTENTS HARMFUL</b><br>Do not swallow.<br>Do not get in eyes or skin or clothing.<br>Keep out of reach of children and pets.<br><b>INGREDIENTS:</b> Propylene Glucol,<br>Vegetable Glycerin, Nicotine (%),<br>Food Grade Alcohol, Natural and<br>Artificial flavours.<br><b>If swallowed consult poison control<br>centre or a doctor immediately.<br>May contain nuts.</b></div>
  <div class="producer producer--left">Produced and Packaged exclusively for:<br>4471920 Ontario Inc, Millbrook ON, L0A 1G0</div>
  <div class="producer producer--right">Produced and Packaged exclusively for:<br>4471920 Ontario Inc, Millbrook ON, L0A 1G0</div>
  <div class="band band--bottom"><span>ZÉRO</span><span>NICOTINE</span><span>ZÉRO</span><span>NICOTINE</span><span>ZÉRO</span><span>NICOTINE</span><span>ZÉRO</span><span>NICOTINE</span><span>ZÉRO</span><span>NICOTINE</span></div>
</section>

<section class="label label--12">
  <div class="band band--top"><span>12 mg/ml</span><span>12 mg/ml</span><span>12 mg/ml</span><span>12 mg/ml</span><span>12 mg/ml</span><span>12 mg/ml</span><span>12 mg/ml</span><span>12 mg/ml</span><span>12 mg/ml</span></div>
  <svg class="hazard" viewBox="0 0 28 28" aria-hidden="true"><polygon points="8,1 20,1 27,8 27,20 20,27 8,27 1,20 1,8" fill="none" stroke="#111" stroke-width="2"/><path d="M8 10 L20 20 M20 10 L8 20" stroke="#111" stroke-width="3" stroke-linecap="round"/></svg>
  <div class="warning warning--fr"><b>CONTENIR NOCIF</b><br>Do not swallow.<br>Do not get in eyes or skin or clothing.<br>Keep out of reach of children and pets.<br><b>INGREDIENTS:</b> Propylene Glucol,<br>Vegetable Glycerin, Nicotine (%),<br>Food Grade Alcohol, Natural and<br>Artificial flavours.<br><b>If swallowed consult poison control<br>centre or a doctor immediately.<br>May contain nuts.</b></div>
  <div class="hero"><div class="hero__watermark">50/50<br>50/50<br>50/50<br>50/50<br>50/50<br>50/50</div><div class="hero__strength"></div><div class="hero__name">k eLiquid</div><div class="hero__volume">12 · 30 ml</div></div>
  <div class="product"><span class="product__light">SWEET</span> <span class="product__bold">TOBACCO</span></div>
  <div class="warning warning--en"><b>WARNING CONTENTS HARMFUL</b><br>Do not swallow.<br>Do not get in eyes or skin or clothing.<br>Keep out of reach of children and pets.<br><b>INGREDIENTS:</b> Propylene Glucol,<br>Vegetable Glycerin, Nicotine (%),<br>Food Grade Alcohol, Natural and<br>Artificial flavours.<br><b>If swallowed consult poison control<br>centre or a doctor immediately.<br>May contain nuts.</b></div>
  <div class="producer producer--left">Produced and Packaged exclusively for:<br>4471920 Ontario Inc, Millbrook ON, L0A 1G0</div>
  <div class="producer producer--right">Produced and Packaged exclusively for:<br>4471920 Ontario Inc, Millbrook ON, L0A 1G0</div>
  <div class="band band--bottom"><span>DANGER</span><span>POISON</span><span>DANGER</span><span>POISON</span><span>DANGER</span><span>POISON</span><span>DANGER</span><span>POISON</span><span>DANGER</span></div>
</section>

<section class="label label--18">
  <div class="band band--top"><span>18 mg/ml</span><span>18 mg/ml</span><span>18 mg/ml</span><span>18 mg/ml</span><span>18 mg/ml</span><span>18 mg/ml</span><span>18 mg/ml</span><span>18 mg/ml</span><span>18 mg/ml</span></div>
  <svg class="hazard" viewBox="0 0 28 28" aria-hidden="true"><polygon points="8,1 20,1 27,8 27,20 20,27 8,27 1,20 1,8" fill="none" stroke="#111" stroke-width="2"/><path d="M8 10 L20 20 M20 10 L8 20" stroke="#111" stroke-width="3" stroke-linecap="round"/></svg>
  <div class="warning warning--fr"><b>CONTENIR NOCIF</b><br>Do not swallow.<br>Do not get in eyes or skin or clothing.<br>Keep out of reach of children and pets.<br><b>INGREDIENTS:</b> Propylene Glucol,<br>Vegetable Glycerin, Nicotine (%),<br>Food Grade Alcohol, Natural and<br>Artificial flavours.<br><b>If swallowed consult poison control<br>centre or a doctor immediately.<br>May contain nuts.</b></div>
  <div class="hero"><div class="hero__watermark">50/50<br>50/50<br>50/50<br>50/50<br>50/50<br>50/50</div><div class="hero__strength"></div><div class="hero__name">k eLiquid</div><div class="hero__volume">18 · 30 ml</div></div>
  <div class="product"><span class="product__light">SWEET</span> <span class="product__bold">TOBACCO</span></div>
  <div class="warning warning--en"><b>WARNING CONTENTS HARMFUL</b><br>Do not swallow.<br>Do not get in eyes or skin or clothing.<br>Keep out of reach of children and pets.<br><b>INGREDIENTS:</b> Propylene Glucol,<br>Vegetable Glycerin, Nicotine (%),<br>Food Grade Alcohol, Natural and<br>Artificial flavours.<br><b>If swallowed consult poison control<br>centre or a doctor immediately.<br>May contain nuts.</b></div>
  <div class="producer producer--left">Produced and Packaged exclusively for:<br>4471920 Ontario Inc, Millbrook ON, L0A 1G0</div>
  <div class="producer producer--right">Produced and Packaged exclusively for:<br>4471920 Ontario Inc, Millbrook ON, L0A 1G0</div>
  <div class="band band--bottom"><span>DANGER</span><span>POISON</span><span>DANGER</span><span>POISON</span><span>DANGER</span><span>POISON</span><span>DANGER</span><span>POISON</span><span>DANGER</span></div>
</section>

<section class="label label--24">
  <div class="band band--top"><span>24 mg/ml</span><span>24 mg/ml</span><span>24 mg/ml</span><span>24 mg/ml</span><span>24 mg/ml</span><span>24 mg/ml</span><span>24 mg/ml</span><span>24 mg/ml</span><span>24 mg/ml</span></div>
  <svg class="hazard" viewBox="0 0 28 28" aria-hidden="true"><polygon points="8,1 20,1 27,8 27,20 20,27 8,27 1,20 1,8" fill="none" stroke="#111" stroke-width="2"/><path d="M8 10 L20 20 M20 10 L8 20" stroke="#111" stroke-width="3" stroke-linecap="round"/></svg>
  <div class="warning warning--fr"><b>CONTENIR NOCIF</b><br>Do not swallow.<br>Do not get in eyes or skin or clothing.<br>Keep out of reach of children and pets.<br><b>INGREDIENTS:</b> Propylene Glucol,<br>Vegetable Glycerin, Nicotine (%),<br>Food Grade Alcohol, Natural and<br>Artificial flavours.<br><b>If swallowed consult poison control<br>centre or a doctor immediately.<br>May contain nuts.</b></div>
  <div class="hero"><div class="hero__watermark">50/50<br>50/50<br>50/50<br>50/50<br>50/50<br>50/50</div><div class="hero__strength"></div><div class="hero__name">k eLiquid</div><div class="hero__volume">24 · 30 ml</div></div>
  <div class="product"><span class="product__light">SWEET</span> <span class="product__bold">TOBACCO</span></div>
  <div class="warning warning--en"><b>WARNING CONTENTS HARMFUL</b><br>Do not swallow.<br>Do not get in eyes or skin or clothing.<br>Keep out of reach of children and pets.<br><b>INGREDIENTS:</b> Propylene Glucol,<br>Vegetable Glycerin, Nicotine (%),<br>Food Grade Alcohol, Natural and<br>Artificial flavours.<br><b>If swallowed consult poison control<br>centre or a doctor immediately.<br>May contain nuts.</b></div>
  <div class="producer producer--left">Produced and Packaged exclusively for:<br>4471920 Ontario Inc, Millbrook ON, L0A 1G0</div>
  <div class="producer producer--right">Produced and Packaged exclusively for:<br>4471920 Ontario Inc, Millbrook ON, L0A 1G0</div>
  <div class="band band--bottom"><span>DANGER</span><span>POISON</span><span>DANGER</span><span>POISON</span><span>DANGER</span><span>POISON</span><span>DANGER</span><span>POISON</span><span>DANGER</span></div>
</section>

</body>
</html>
```